Best in class cloud software provider for retailers needs a new business card design to reflect prod

We are a software company based out of Chicago selling into retailers. We have a new website and marketing collateral that support our new product designs. We are obsessed with simplicity, ease of use, and having a really powerful product set. We have two products as noted on our website - www.brolvane.com - one is a retail task management product and the other is a Help Ticketing product.

At Brolvane we are passionate about creating the best Retail Task Management system in the industry. We bring more than 20 years of retail operations, Workforce Management and Retail Task experience and have a set of web and mobile software features that no one else has. Brolvane enables you to plan and distribute work throughout your organization and ensure it gets done.

We need a new business card design that reflects our new branding, message and approach.

I've attached a few documents that help support what we are building and how our colors look.

There may be additional future work if this goes well.

Thanks,
Mark

President

Target Market(s)

We sell into retailers and are a software company

Industry/Entity Type

Software

Contact Information for Business Card

The card must have

Name
title
address
tele
email
Brolvane logo (someplace)

So for example

It would have for me

Mark Dorsett
President
48 West Harlow Ave. Suite 310
Chicago, IL 60687
3125550187
mdorsett@brolvane.com

Requirements
Must have
• We need to cards for 5 different people - same design different names etc
Nice to have
• should reflect our colors and product and website - be creative - ease of use, simplicity, and power is what the product is about - but we are very forward Brolvane and hear all the time that our product is gorgeous. The font should be consistent with our website, and marketing one pager included
Should not have
• Strange or unfamiliar colors or fonts...

```html
<!DOCTYPE html>
<html lang="en">
<head>
<meta charset="UTF-8">
<title>Brolvane Business Card</title>
<link rel="stylesheet" href="https://fonts.googleapis.com/css2?family=Open+Sans:wght@400;600;700&display=swap">
<style>
  :root {
    --brand-blue: #1f6f9b;
    --brand-blue-light: #4a93b6;
    --brand-blue-dark: #1a5f87;
    --stripe-grey: #3b3d40;
    --paper-white: #fbfbfa;
    --backdrop: #d9dadb;
    --text-white: #ffffff;
    --icon-dark: #2c3236;
  }
  * { box-sizing: border-box; margin: 0; padding: 0; }
  html, body {
    width: 1200px; height: 800px; overflow: hidden;
    background: var(--backdrop);
    font-family: "Open Sans", Arial, sans-serif;
  }
  .canvas { position: relative; width: 1200px; height: 800px; }

  .card {
    position: absolute; width: 620px; height: 354px; overflow: hidden;
    box-shadow: 0 10px 24px rgba(0,0,0,0.25);
  }

  /* Back side */
  .card--back {
    left: 80px; top: 50px;
    background: radial-gradient(ellipse at 65% 30%, var(--brand-blue-light) 0%, var(--brand-blue) 55%, var(--brand-blue-dark) 100%);
    display: flex; flex-direction: column; align-items: center; justify-content: center;
    color: var(--text-white);
  }
  .card--back .wordmark { font-size: 84px; font-weight: 700; letter-spacing: -1px; line-height: 1; }
  .card--back .wordmark sup { font-size: 12px; font-weight: 600; vertical-align: top; margin-left: 2px; }
  .card--back .back-url { font-size: 15px; margin-top: 6px; letter-spacing: 0.3px; }

  /* Front side */
  .card--front {
    left: 500px; top: 400px;
    background: var(--paper-white);
  }
  .front-header {
    position: absolute; left: 0; top: 0; width: 100%; height: 168px;
    display: flex; align-items: flex-end; padding: 0 0 22px 40px;
  }
  .front-header .wordmark {
    font-size: 92px; font-weight: 700; color: var(--brand-blue);
    letter-spacing: -1.5px; line-height: 1;
  }
  .front-header .wordmark sup { font-size: 12px; font-weight: 600; vertical-align: top; margin-left: 2px; }
  .front-stripe {
    position: absolute; left: 0; top: 168px; width: 100%; height: 9px;
    background: var(--stripe-grey);
  }
  .front-panel {
    position: absolute; left: 0; top: 177px; width: 100%; height: 177px;
    background: radial-gradient(ellipse at 45% 10%, var(--brand-blue-light) 0%, var(--brand-blue) 55%, var(--brand-blue-dark) 100%);
    color: var(--text-white);
  }
  .person {
    position: absolute; left: 40px; bottom: 26px;
    font-size: 15px; line-height: 1.3;
  }
  .person .person-name { font-size: 25px; font-weight: 400; line-height: 1.15; }
  .panel-divider {
    position: absolute; left: 372px; top: 24px; width: 2px; height: 118px;
    background: var(--stripe-grey);
  }
  .contacts {
    position: absolute; right: 28px; top: 26px;
    list-style: none; text-align: right; font-size: 15px; line-height: 1.55;
  }
  .contacts li { display: flex; align-items: center; justify-content: flex-end; gap: 8px; }
  .contacts svg { width: 16px; height: 14px; flex: none; }
</style>
</head>
<body>
<main class="canvas">

  <section class="card card--back" aria-label="Business card back">
    <div class="wordmark">Brolvane<sup>TM</sup></div>
    <div class="back-url">www.brolvane.com</div>
  </section>

  <section class="card card--front" aria-label="Business card front">
    <header class="front-header">
      <div class="wordmark">Brolvane<sup>TM</sup></div>
    </header>
    <div class="front-stripe"></div>
    <div class="front-panel">
      <div class="person">
        <div class="person-name">Mark Dorsett</div>
        <div class="person-title">President</div>
        <div class="person-address">48 West Harlow Ave. Suite 310</div>
        <div class="person-city">Chicago, IL 60687</div>
      </div>
      <div class="panel-divider"></div>
      <ul class="contacts">
        <li>3125550187
          <svg viewBox="0 0 16 14" aria-hidden="true"><path d="M2 5 Q8 0 14 5 L12 7 L10 5 L6 5 L4 7 Z M4 8 H12 L13 13 H3 Z" fill="var(--icon-dark)"/></svg>
        </li>
        <li>mdorsett@brolvane.com
          <svg viewBox="0 0 16 14" aria-hidden="true"><rect x="1" y="2" width="14" height="10" fill="var(--icon-dark)"/><path d="M1 2 L8 8 L15 2" stroke="#fff" stroke-width="1.2" fill="none"/></svg>
        </li>
        <li>www.brolvane.com
          <svg viewBox="0 0 16 14" aria-hidden="true"><rect x="1.5" y="1.5" width="13" height="9" fill="none" stroke="var(--icon-dark)" stroke-width="1.5"/><rect x="5" y="11.5" width="6" height="1.5" fill="var(--icon-dark)"/></svg>
        </li>
      </ul>
    </div>
  </section>

</main>
</body>
</html>
```